依頼詳細
「北辰年金事務研究連盟」の概要・活動内容等を紹介するパンフレットの作成です。パンフレットとはいえ、A4裏表の簡易版でOKです(ページ数2ページ)。全体として、固い厳粛なイメージが出ればよいかと思います。記載する文章等は添付ファイルのとおりですので、配置や色、デザイン等の作成をお願いします。アレンジはお任せします。
記載項目
北辰年金事務研究連盟/ごあいさつ/協議会概要/活動内容(原則、添付ファイルの通り)
サイズ
A4
ページ数
両面
希望イメージ
シンプル 複雑
単色 カラフル
暗い 明るい
日常 高級
遊び心 厳粛
未来的 伝統的
女性的 男性的
希望する色
青系、茶系、グレー系、全体のバランスがよければ必ずしも上記に拘らないです。
納品ファイル
• PNG形式 (.png)
補足説明
協議会のWEBサイトは以下です。
http://hokushin-renmei.net/
内容やイメージの参考にしてください。

やや硬いイメージを保ちつつ、シンプルで分かりやすいという点を判断基準として、選択いたしました。ありがとうございます。

この度は、多くのランサーの方からご提案いただき、大変ありがとうございます。改めて感謝申し上げます。
途中、修正依頼させていただいた方におかれましては、実際の選択ポイントからずれた内容で依頼してしまったこともあり、この点、お詫び申し上げます。(私以外の担当の意見も反映したことによるものです。何卒ご容赦ください。)
今後また案件が発生した際には、ご協力いただければ幸いです。
どうぞ宜しくお願いします。

```html
<!DOCTYPE html>
<html lang="ja">
<head>
<meta charset="utf-8">
<title>北辰年金事務研究連盟 ごあいさつ</title>
<link rel="stylesheet" href="https://fonts.googleapis.com/css2?family=Noto+Serif+JP:wght@400;600;700;900&display=swap">
<style>
  :root {
    --brown-dark: #3f2a1f;
    --brown: #5a3d2c;
    --gold: #d8b66a;
    --paper: #ffffff;
    --ink: #2b2522;
    --illus-light: #f6f1ea;
    --illus-mid: #e6dccd;
    --illus-green: #c9d6a8;
  }
  * { margin: 0; padding: 0; box-sizing: border-box; }
  html, body { width: 849px; height: 1200px; overflow: hidden; background: var(--paper); }
  .page {
    position: relative; width: 849px; height: 1200px;
    font-family: "Noto Serif JP", serif; color: var(--ink);
  }
  .masthead {
    position: absolute; left: 0; top: 0; width: 849px; height: 118px;
    background: linear-gradient(180deg, var(--brown) 0%, var(--brown-dark) 100%);
    border-bottom: 2px solid var(--gold);
  }
  .masthead .mark {
    position: absolute; left: 22px; top: 14px; width: 50px; height: 42px;
    border-radius: 6px; background: var(--gold);
  }
  .masthead .org-name {
    position: absolute; left: 90px; top: 8px;
    font-size: 36px; font-weight: 900; color: #fff; letter-spacing: 2px;
  }
  .masthead .tagline {
    position: absolute; left: 90px; top: 64px;
    font-size: 22px; font-weight: 700; color: var(--gold); letter-spacing: 1px;
  }
  .hero-illustration {
    position: absolute; left: 440px; top: 160px; width: 360px; height: 400px;
    background: radial-gradient(ellipse at 55% 55%, var(--illus-mid) 0%, var(--illus-light) 55%, rgba(255,255,255,0) 75%);
  }
  .hero-illustration::after {
    content: ""; position: absolute; left: 120px; top: 250px; width: 90px; height: 60px;
    border-radius: 50%; background: radial-gradient(var(--illus-green), rgba(255,255,255,0) 70%);
  }
  .greeting {
    position: absolute; left: 160px; top: 232px; width: 585px;
    font-size: 14px; line-height: 25px; text-align: justify;
  }
  .greeting .spacer { float: right; width: 200px; height: 300px; }
  .greeting h2 { font-size: 17px; font-weight: 600; margin-bottom: 24px; }
  .greeting p { text-indent: 1em; margin-bottom: 25px; }
  .signature {
    position: absolute; right: 105px; top: 1040px; text-align: right;
  }
  .signature .org { font-size: 14px; }
  .signature .rep { margin-top: 10px; font-size: 14px; }
  .signature .rep span { font-size: 26px; font-weight: 700; margin-left: 18px; letter-spacing: 4px; }
  .footer-band {
    position: absolute; left: 0; bottom: 0; width: 849px; height: 34px;
    background: linear-gradient(180deg, var(--brown) 0%, var(--brown-dark) 100%);
    border-top: 2px solid var(--gold);
  }
</style>
</head>
<body>
<div class="page">
  <header class="masthead">
    <div class="mark"></div>
    <h1 class="org-name">北辰年金事務研究連盟</h1>
    <p class="tagline">社保調査の専門家「社会保険労務士」による全国組織</p>
  </header>

  <div class="hero-illustration" role="img" aria-label="木の家の模型と小さな緑の芽を淡い色調で描いたイメージ"></div>

  <section class="greeting">
    <div class="spacer"></div>
    <h2>ごあいさつ</h2>
    <p>北辰年金事務研究連盟／代表の山科でございます。</p>
    <p>昨今、厚生労働省(日本年金機構)による、社会保険の取り締まりが一段と厳しさを増してきております。具体的には、法人でありながら社会保険に加入していないいわゆる"加入逃れ"、あるいは社会保険には加入しているが、対象者全員を加入させていないいわゆる"加入漏れ"――こういった企業に対する取り締まりが強化されています。</p>
    <p>当然ではありますが、今後は、中小規模の企業様におかれましても、社会保険に適正に加入することを前提として、経営を考えていかなければならないといえるでしょう。</p>
    <p>このような問題を踏まえ、我々開業社会保険労務士がチームを組み、社会保険への適正加入の促進活動を行なっていくことを目的として、この度、「北辰年金事務研究連盟」を設立させていただいた次第でございます。</p>
    <p>ただ、一方で社会保険の負担が非常に重いという問題もありますので、その中で、いかにして負担を軽減しながら、適正な形で社会保険に加入することができるかといった視点に立ち、企業経営者の方とともに解決策を模索していくアドバイザー的な役割として、各種サービスをご提供させていただければと考えております。</p>
    <p>今後、当協議会の活動にご期待ください。今後とも宜しくお願い申し上げます。</p>
  </section>

  <div class="signature">
    <p class="org">北辰年金事務研究連盟</p>
    <p class="rep">代表<span>山科 透</span></p>
  </div>

  <div class="footer-band"></div>
</div>
</body>
</html>
```